Simple, Professional and neat business card design for Vellamor Inc.

We're looking to re-vamp our business card design. We're a supplier of innovative feed ingredients for the North American animal agriculture industry. We are located in Lucknow, Ontario, Canada and our flagship product is a product that prevents milk fever in dairy cows when the calve, it is fed before calving and is very effective compared to other alternatives available on the market today.

Our company has Danish roots and we import all of our product from our Danish partner/manufacturer in Denmark. We like our design to embrace high professionalism while remaining neat and simple.

Target Market(s)

B2B, Feed Mills, Veterinary Clinics, Large integrators/producers,

Industry/Entity Type

Agribusiness

Contact Information for Business Card

We like the rounded corners because they make the card easy to sit in a wallet and not many use it so it makes the card stand out, just possibly something to take account for during the design.

As you can also see on the sliders below, looking for a that simple but proffesional scandinavian design.

Requirements
Nice to have
• Rounded corners
Should not have
• Too vibrant

```html
<!DOCTYPE html>
<html lang="en">
<head>
<meta charset="utf-8">
<title>Vellamor Inc. — Business Card</title>
<link href="https://fonts.googleapis.com/css2?family=Lato:wght@400;700;900&display=swap" rel="stylesheet">
<style>
  :root {
    --backdrop: #55585d;
    --card: #17181b;
    --brand-blue: #0b6fbe;
    --label-blue: #1e73c4;
    --text-light: #f2f2f2;
  }
  * { margin: 0; padding: 0; box-sizing: border-box; }
  html, body {
    width: 1200px; height: 1200px; overflow: hidden;
    background: var(--backdrop);
    font-family: "Lato", sans-serif;
  }
  .sheet {
    position: relative; width: 1200px; height: 1200px;
    display: flex; flex-direction: column; align-items: center;
    justify-content: center; gap: 44px;
  }
  .card {
    position: relative; width: 860px; height: 491px;
    background: var(--card); border-radius: 40px; overflow: hidden;
    box-shadow: 0 18px 40px rgba(0,0,0,.35);
  }
  .brand-mark {
    width: 64px; height: 64px; border-radius: 50%;
    background: var(--brand-blue); flex: none;
  }
  .brand-name {
    color: var(--brand-blue); font-weight: 900; font-size: 46px;
    letter-spacing: 1px; text-transform: uppercase; white-space: nowrap;
  }
  /* front */
  .card--front .brand-lockup {
    position: absolute; left: 120px; top: 50%; transform: translateY(-50%);
    display: flex; align-items: center; gap: 22px;
  }
  /* back */
  .card--back .brand-block {
    position: absolute; left: 50px; top: 70px; width: 400px;
    display: flex; flex-direction: column; align-items: center; gap: 40px;
  }
  .card--back .brand-mark { width: 190px; height: 190px; }
  .card--back .brand-name { font-size: 44px; }
  .divider {
    position: absolute; left: 0; top: 0; width: 860px; height: 491px;
  }
  .contact {
    position: absolute; left: 495px; top: 70px; width: 345px;
    color: var(--text-light); font-size: 17px; line-height: 1.3;
    white-space: nowrap;
  }
  .contact__name {
    color: var(--label-blue); font-weight: 900; font-size: 28px;
    text-transform: uppercase; margin-bottom: 18px; letter-spacing: .3px;
  }
  .contact__address { margin-bottom: 22px; }
  .contact__label { color: var(--label-blue); }
  .contact__row { margin-bottom: 5px; }
  .band {
    position: absolute; left: 0; bottom: 0; width: 100%; height: 44px;
    background: var(--brand-blue);
  }
</style>
</head>
<body>
<main class="sheet">
  <section class="card card--front">
    <div class="brand-lockup">
      <span class="brand-mark"></span>
      <span class="brand-name">Vellamor Inc.</span>
    </div>
  </section>

  <section class="card card--back">
    <div class="brand-block">
      <span class="brand-mark"></span>
      <span class="brand-name">Vellamor Inc.</span>
    </div>
    <svg class="divider" viewBox="0 0 860 491" aria-hidden="true">
      <defs>
        <linearGradient id="divider-fade" x1="0" y1="0" x2="0" y2="1">
          <stop offset="0" stop-color="#1e73c4" stop-opacity="0"/>
          <stop offset=".5" stop-color="#1e73c4" stop-opacity=".9"/>
          <stop offset="1" stop-color="#1e73c4" stop-opacity="0"/>
        </linearGradient>
      </defs>
      <line x1="462" y1="120" x2="480" y2="420" stroke="url(#divider-fade)" stroke-width="1.5"/>
    </svg>
    <div class="contact">
      <div class="contact__name">Anders Holmgaard</div>
      <div class="contact__address"><span class="contact__label">Address:</span> Box 412, Harrowdale, Westmark<br>Norland R4T 1P8</div>
      <div class="contact__row"><span class="contact__label">Mobile:</span> 555 . 301 . 0147</div>
      <div class="contact__row"><span class="contact__label">Office:</span> 555 . 301 . 0162</div>
      <div class="contact__row"><span class="contact__label">Toll Free:</span> 800 . 555 . 0190</div>
      <div class="contact__row"><span class="contact__label">Fax:</span> 555 . 301 . 0175</div>
      <div class="contact__row"><span class="contact__label">Email:</span> anders@vellamor.com</div>
      <div class="contact__row"><span class="contact__label">Web:</span> www.vellamor.com</div>
    </div>
    <div class="band"></div>
  </section>
</main>
</body>
</html>
```